BrambleWorks business card

Looking for business card design that supports our company/software values. We have 2 logo designs at the moment but open to change if you think you can enhance the brand. Check out website www.brambleworks.com.au.

Target Market(s)

Education

Contact Information for Business Card

Name, title, mobile, email and website

Font styles to use
Sans Serif

Colors

Designer to choose colors to be used in the design.

Requirements
Must have
• BrambleWorks logo with tree and tagline on rear side with dark grey background colour

```html
<!DOCTYPE html>
<html lang="en">
<head>
<meta charset="utf-8">
<title>BrambleWorks business card</title>
<link rel="stylesheet" href="https://fonts.googleapis.com/css2?family=Arimo:wght@400;700&family=Open+Sans:wght@400&display=swap">
<style>
  :root {
    --page-bg: #e9e7e3;
    --card-green: #4f7d21;
    --card-grey: #4b4b4b;
    --text-light: #f2f5ee;
    --text-dark: #101a08;
    --wordmark-light: #e6e6e6;
  }
  * { box-sizing: border-box; margin: 0; padding: 0; }
  html, body {
    width: 1200px;
    height: 900px;
    overflow: hidden;
    background: var(--page-bg);
  }
  .sheet {
    width: 1200px;
    height: 900px;
    display: flex;
    align-items: center;
    justify-content: center;
    gap: 40px;
  }
  .card {
    width: 540px;
    height: 309px;
    position: relative;
    box-shadow: 0 8px 20px rgba(0, 0, 0, 0.18);
  }
  .card--front { background: var(--card-green); }
  .card--back  { background: var(--card-grey); }

  .front-brand {
    position: absolute;
    top: 26px;
    left: 34px;
    display: flex;
    align-items: center;
    gap: 8px;
    font-family: "Arimo", Arial, sans-serif;
    font-size: 15px;
    color: var(--text-light);
  }
  .brand-dot {
    width: 10px;
    height: 10px;
    border-radius: 50%;
    background: var(--text-light);
  }
  .contact {
    position: absolute;
    top: 96px;
    left: 34px;
    font-family: "Arimo", Arial, sans-serif;
    color: var(--text-light);
    font-size: 12.5px;
    line-height: 1.3;
  }
  .contact__name {
    font-weight: 700;
    font-size: 17px;
    color: var(--text-dark);
    margin-bottom: 4px;
  }

  .back-brand {
    position: absolute;
    inset: 0;
    display: flex;
    flex-direction: column;
    align-items: center;
    justify-content: center;
    gap: 18px;
  }
  .back-brand__mark {
    width: 64px;
    height: 64px;
    border-radius: 50%;
    background: var(--wordmark-light);
  }
  .back-brand__name {
    font-family: "Open Sans", Arial, sans-serif;
    font-size: 32px;
    letter-spacing: 0.5px;
    color: var(--wordmark-light);
  }
</style>
</head>
<body>
  <main class="sheet">
    <section class="card card--front" aria-label="Card front">
      <div class="front-brand">
        <span class="brand-dot"></span>
        <span>BrambleWorks</span>
      </div>
      <div class="contact">
        <p class="contact__name">Sample Name</p>
        <p>Suite 5</p>
        <p>123 Street</p>
        <p>Tel: 0755018442</p>
        <p>Email: hello@brambleworks.com.au</p>
        <p>www.brambleworks.com.au</p>
      </div>
    </section>

    <section class="card card--back" aria-label="Card back">
      <div class="back-brand">
        <span class="back-brand__mark"></span>
        <span class="back-brand__name">BrambleWorks</span>
      </div>
    </section>
  </main>
</body>
</html>
```